Korvune Site

We are looking for someone to help build a information site of our product Korvune for Sickle Cell Disease

Industry/Entity Type

Patent Educational Site

Coding

Coded - Design and coding required

Number of Pages Required

5+ page

Font styles to use
Sans Serif

Colors
EB3D1F
EC4F4E
F09395
F8D3D4
FCEDEE

```html
<!DOCTYPE html>
<html lang="en">
<head>
<meta charset="utf-8">
<title>Korvune – Medical Food for Sickle Cell Disease</title>
<link rel="stylesheet" href="https://fonts.googleapis.com/css2?family=Poppins:wght@400;500;600&family=Playfair+Display:wght@500&family=Great+Vibes&display=swap">
<style>
:root{
  --brand:#EB3D1F;
  --brand-soft:#EC4F4E;
  --rose:#F09395;
  --blush:#F8D3D4;
  --mist:#FCEDEE;
  --ink:#333338;
  --ink-soft:#55555c;
  --white:#ffffff;
}
*{box-sizing:border-box;margin:0;padding:0}
html,body{width:749px;height:1200px;overflow:hidden;background:var(--white)}
body{font-family:"Poppins",sans-serif;color:var(--ink);position:relative}
a{color:inherit;text-decoration:none}

.announce{height:24px;background:var(--brand);color:var(--white);font-size:9.4px;display:flex;align-items:center;padding-left:70px;position:relative}
.announce strong{font-weight:600;margin-right:3px}
.announce .partner-badge{position:absolute;right:69px;top:0;width:34px;height:24px;background:var(--white)}

.site-header{height:55px;display:flex;align-items:center;padding:0 70px}
.brand-name{font-size:24px;font-weight:500;color:var(--brand);letter-spacing:.5px}
.main-nav{margin-left:auto;display:flex;gap:13px;font-size:10.2px;color:var(--ink)}

.hero{position:relative;height:346px;overflow:hidden;background:radial-gradient(ellipse at 72% 60%,#a01a1e 0%,#4a1014 35%,#1b1a1b 70%,#0f1012 100%)}
.hero-art{position:absolute;inset:0}
.hero-copy{position:absolute;left:71px;top:68px;color:var(--white)}
.hero-script{font-family:"Great Vibes",cursive;font-size:31px;line-height:1}
.hero-title{font-family:"Playfair Display",serif;font-weight:500;font-size:30px;letter-spacing:.5px;margin-top:8px}
.hero-text{font-size:10.5px;line-height:17px;margin-top:17px;width:340px}
.hero-btn{display:inline-flex;align-items:center;justify-content:center;margin-top:20px;width:124px;height:40px;border-radius:20px;background:var(--brand);font-weight:600;font-size:11.5px}

.topic-cards{display:flex;gap:7.5px;padding:6px 5px 0}
.topic-card{flex:1;background:var(--mist)}
.topic-media{height:125px}
.topic-label{height:29px;display:flex;align-items:center;justify-content:center;font-size:10.8px;font-weight:500;color:var(--ink)}

.advice{text-align:center;font-size:12px;line-height:20px;color:var(--ink-soft);margin-top:36px}

.act-band{position:absolute;top:697px;left:0;width:749px;height:290px;background:radial-gradient(ellipse at 30% 40%,#ee3a2e 0%,#d4231f 45%,#b51c1a 100%);color:var(--white);display:flex;align-items:center;justify-content:center}
.act-band p{width:640px;text-align:center;font-size:10.2px;line-height:17.1px}

.site-footer{position:absolute;top:1020px;left:70px;right:70px}
.footer-cols{display:flex}
.footer-brand{width:181px;padding-top:10px}
.footer-brand .brand-name{font-size:28px}
.footer-links{width:160px}
.footer-head{font-size:11.5px;font-weight:500;margin-bottom:8px}
.footer-links li{list-style:none;font-size:10.2px;line-height:16.6px;color:var(--ink-soft)}
.contact-row{display:flex;gap:10px;font-size:10.2px;line-height:13.5px;color:var(--ink-soft);margin-bottom:12px}
.contact-row svg{flex:none;margin-top:1px}
.footer-bottom{margin-top:10px;border-top:1px solid #cfcfd3;padding-top:15px;display:flex;align-items:center}
.copyright{font-size:10.2px;color:var(--ink-soft)}
.social{margin-left:auto;display:flex;gap:3px}
.social span{width:21px;height:21px;border:1px solid var(--brand);border-radius:50%}
</style>
</head>
<body>

<div class="announce"><strong>Coming Soon:</strong> A Medical Food for the Dietary Management of Sickle Cell Disease in Pediatric and Adult Patients
  <span class="partner-badge" role="img" aria-label="Partner badge"></span>
</div>

<header class="site-header">
  <a class="brand-name" href="#">Korvune</a>
  <nav class="main-nav">
    <a href="#">What is Korvune</a><a href="#">About SCD</a><a href="#">How Korvune Works</a><a href="#">Insurance Coverage</a><a href="#">Patient Support</a>
  </nav>
</header>

<section class="hero">
  <div class="hero-art" role="img" aria-label="Illustration of red blood cells and sickle-shaped cells flowing in a vessel"></div>
  <div class="hero-copy">
    <div class="hero-script">Korvune for</div>
    <h1 class="hero-title">SICKLE CELL DISEASE</h1>
    <p class="hero-text">Korvune is a medical food emulsification formulated to provide a high concentration of triglycerides of certain fatty acids.</p>
    <a class="hero-btn" href="#">GET MORE INFO</a>
  </div>
</section>

<section class="topic-cards">
  <a class="topic-card" href="#"><div class="topic-media" role="img" aria-label="Photo of a mother giving her child a spoonful of medicine" style="background:linear-gradient(135deg,#d9c8b8,#8a5a3c)"></div><div class="topic-label">What is Korvune</div></a>
  <a class="topic-card" href="#"><div class="topic-media" role="img" aria-label="Illustration of round and sickle red blood cells on dark red" style="background:radial-gradient(circle at 50% 50%,#8e0d10,#3a0406)"></div><div class="topic-label">About Sickle Cell Disease</div></a>
  <a class="topic-card" href="#"><div class="topic-media" role="img" aria-label="Close-up of a sickle cell beside a normal red blood cell" style="background:linear-gradient(90deg,#0b0b0b 0%,#c21318 30%,#1a0000 50%,#d8181d 75%,#0b0b0b 100%)"></div><div class="topic-label">How Korvune Works</div></a>
  <a class="topic-card" href="#"><div class="topic-media" role="img" aria-label="Photo of health insurance forms with the words health coverage options" style="background:linear-gradient(135deg,#2a3038,#8f98a3)"></div><div class="topic-label">Insurance Coverage</div></a>
  <a class="topic-card" href="#"><div class="topic-media" role="img" aria-label="Photo of a caregiver comforting a patient" style="background:linear-gradient(135deg,#c9a98e,#6e3b4a)"></div><div class="topic-label">Patient Support</div></a>
</section>

<p class="advice">Ask your doctor or dietitian for more information about Korvune®.<br>Use under medical supervision.</p>

<section class="act-band">
  <p>The Congress of the United States enacted Orphan Drug Act (21 U.S.C. 360ee(b)(3)) which stated in section 5(b)(3) that a new category of treatment for a small number of diseases, one of which was sickle cell disease, is now allowed. These treatment modalities require clinical and scientific evidence before they can enter commerce, but the Act also allows such products to become available through an abbreviated process, avoiding the high cost of a New Drug Application.&nbsp; The term medical food, as defined in section 5(b) of the Orphan Drug Act is "a food which is formulated to be consumed or administered enterally (by mouth) under the supervision of a physician and which is intended for the specific dietary management of a disease or condition for which distinctive nutritional requirements, based on recognized scientific principles, are established by medical evaluation."&nbsp; Marrowell and Company, the creator of Korvune®, began research on sickle cell disease in 2011.&nbsp; From over a decade of work, Korvune® was created and will soon become available globally in 2023. Korvune® is a Medical Food that is intended to restore the balance in the cellular membrane of people with sickle cell disease and may have a significant beneficial effect.</p>
</section>

<footer class="site-footer">
  <div class="footer-cols">
    <div class="footer-brand"><span class="brand-name">Korvune</span></div>
    <div class="footer-links">
      <h3 class="footer-head">Quick Links</h3>
      <ul><li>What is Korvune</li><li>About SCD</li><li>How Korvune Works</li><li>Insurance Coverage</li><li>Patient Support</li></ul>
    </div>
    <div class="footer-contact">
      <h3 class="footer-head">Contact Us</h3>
      <div class="contact-row"><svg width="8" height="11" viewBox="0 0 8 11"><path d="M4 0a4 4 0 0 0-4 4c0 3 4 7 4 7s4-4 4-7a4 4 0 0 0-4-4zm0 5.5A1.5 1.5 0 1 1 4 2.5a1.5 1.5 0 0 1 0 3z" fill="#EB3D1F"/></svg><span>No: 123emo enim ipsam volupta<br>tem quia voluptas sit aspe</span></div>
      <div class="contact-row"><svg width="10" height="10" viewBox="0 0 10 10"><path d="M2 0l2 2.5-1.2 1.2a6 6 0 0 0 3.5 3.5L7.5 6 10 8 8.5 9.8C4 9.5.5 6 .2 1.5z" fill="#EB3D1F"/></svg><span>1 800 555 0142</span></div>
      <div class="contact-row"><svg width="11" height="9" viewBox="0 0 11 9"><rect width="11" height="9" rx="1" fill="#EB3D1F"/><path d="M.5 1l5 3.5 5-3.5" stroke="#fff" fill="none"/></svg><span>info@corvalis.com</span></div>
    </div>
  </div>
  <div class="footer-bottom">
    <span class="copyright">© 2023, Korvune. All Rights Reserved.</span>
    <div class="social"><span aria-label="Social link 1"></span><span aria-label="Social link 2"></span><span aria-label="Social link 3"></span><span aria-label="Social link 4"></span></div>
  </div>
</footer>

</body>
</html>
```